Web Design Project

We are an IT System Integrator. We provide Quillon 450 ERP System, CRM etc. We also provide hardware, networking servicing. Please look at www.trevantech.com.sg. They provide the same service as us. We like to redesign our web site. I will attached the color that I prefer for reference.
Updates

Our website is www.korbix.com.sg.  It has been created about 14 years ago.  We are trying to revamp it with a new look and information.   The new website must be informative, fast.    I have attached an attachment which show the color that I prefer(brownish golden).   

Our competitor (www.trevantech.com) is carrying the same trade as us.  They have all the informations In their website that we will like to have.  Therefore I recommend you to take a look at my competitor website and have a better   
understanding on the kind of information I would like to have for my new website.

This project is guarantee to the person with the best design.  We can have it guarantee.

Target Market(s)

Corporate and companies

Industry/Entity Type

Hardware

```html
<!DOCTYPE html>
<html lang="en">
<head>
<meta charset="utf-8">
<title>KORBIX – IT System Integrator</title>
<link rel="stylesheet" href="https://fonts.googleapis.com/css2?family=Didact+Gothic&family=Carlito:wght@400;700&family=Arimo&display=swap">
<style>
  :root{
    --ink:#333333;
    --body-text:#3d3d3d;
    --gold-top:#e9bf3f;
    --gold-bottom:#d9a826;
    --nav-text:#3a3524;
    --nav-active:#fff8e6;
    --teal-light:#e3f2f3;
    --teal-mid:#c6e3e5;
    --frame:#5d6466;
    --caption-bg:rgba(40,44,48,.72);
    --white:#ffffff;
  }
  *{box-sizing:border-box;margin:0;padding:0}
  html,body{width:1200px;height:1000px;overflow:hidden}
  body{position:relative;background:var(--white);font-family:"Carlito",sans-serif;color:var(--ink)}

  .site-header{position:absolute;left:0;top:0;width:1200px;height:127px;background:var(--white);overflow:hidden}
  .brand{position:absolute;left:28px;top:28px;display:flex;align-items:center;gap:14px;color:var(--ink);font-family:"Carlito",sans-serif;font-weight:400}
  .brand-mark{width:44px;height:44px;background:var(--gold-bottom)}
  .brand-name{font-size:54px;line-height:54px;letter-spacing:1px}
  .brand-tag{font-size:20px;line-height:22px}
  .utility-links{position:absolute;right:41px;top:16px;font-family:"Arimo",sans-serif;font-size:14px;color:#222}
  .search-box{position:absolute;left:938px;top:67px;width:222px;height:38px;border:1px solid #222;background:var(--white);display:flex;align-items:center;gap:8px;padding-left:6px;font-family:"Arimo",sans-serif;font-size:20px;color:#888}

  .main-nav{position:absolute;left:0;top:127px;width:1200px;height:64px;background:linear-gradient(var(--gold-top),var(--gold-bottom));display:flex;justify-content:center;align-items:center;gap:38px;font-family:"Didact Gothic",sans-serif;font-size:34px;color:var(--nav-text);box-shadow:0 2px 3px rgba(0,0,0,.15)}
  .main-nav .active{color:var(--nav-active)}

  .page{position:absolute;left:0;top:191px;width:1200px;height:809px;background:radial-gradient(ellipse at 70% 50%,var(--teal-light),var(--teal-mid) 75%,#b9dadd)}

  .hero{position:absolute;left:110px;top:42px;width:1008px;height:416px;border:3px solid var(--frame);border-radius:3px;overflow:hidden;background:linear-gradient(100deg,#3b5670,#8fa6bd 45%,#c9d6e2 70%,#6f8aa6)}
  .hero-caption{position:absolute;left:0;bottom:0;width:100%;height:104px;background:var(--caption-bg);text-align:center;color:var(--white)}
  .hero-quote{font-size:28px;padding-top:24px}
  .hero-dots{position:absolute;left:462px;top:71px;display:flex;gap:4px}
  .dot{width:16px;height:16px;border-radius:50%;border:2px solid #ddd;background:rgba(0,0,0,.25)}
  .dot.current{background:#ddd}

  .tile{position:absolute;left:110px;width:302px;border:3px solid var(--white);overflow:hidden}
  .tile-title{position:absolute;left:8px;top:0;font-size:40px;font-weight:400;color:var(--white);line-height:44px}
  .news{top:495px;height:216px;background:linear-gradient(#6a6e72,#3a3d40)}
  .news-caption{position:absolute;left:0;bottom:0;width:100%;padding:0 12px 3px;background:rgba(20,20,20,.6);color:var(--white);font-size:16px;line-height:20px;text-align:right}
  .news-caption .more{display:block;text-align:right;font-size:12px;line-height:12px}
  .products{top:733px;height:90px;background:linear-gradient(#2d3b4a,#6b7c8d)}

  .welcome{position:absolute;left:452px;top:495px;width:661px;color:var(--body-text)}
  .welcome h1{font-weight:400;font-size:42px;line-height:46px;margin-bottom:14px;color:#444}
  .welcome p{font-size:17.6px;line-height:21.4px;text-align:justify;text-indent:42px;margin-bottom:21px}
</style>
</head>
<body>
  <header class="site-header">
    <div class="brand">
      <span class="brand-mark" aria-hidden="true"></span>
      <div>
        <div class="brand-name">KORBIX</div>
        <div class="brand-tag">IT System Integrator</div>
      </div>
    </div>
    <div class="utility-links">Contact us | Help | FAQs</div>
    <div class="search-box">
      <svg width="32" height="32" viewBox="0 0 32 32" aria-hidden="true"><circle cx="13" cy="13" r="10" fill="#dfe9f2" stroke="#666" stroke-width="2.5"/><line x1="20" y1="20" x2="29" y2="29" stroke="#444" stroke-width="4" stroke-linecap="round"/></svg>
      <span>Search here...</span>
    </div>
  </header>

  <nav class="main-nav">
    <span class="active">HOME</span><span>|</span><span>ABOUT US</span><span>|</span><span>SERVICES</span><span>|</span><span>CLIENTS</span>
  </nav>

  <main class="page">
    <section class="hero" role="img" aria-label="Photo of two IT engineers reviewing a laptop in a server room">
      <div class="hero-caption">
        <p class="hero-quote">“Abiding and reliable long-term business relationships.”</p>
        <div class="hero-dots"><span class="dot current"></span><span class="dot"></span><span class="dot"></span><span class="dot"></span><span class="dot"></span></div>
      </div>
    </section>

    <article class="tile news" role="img" aria-label="Photo of business partners toasting at a workshop event">
      <h2 class="tile-title">News</h2>
      <p class="news-caption">Expanding the Boundaries with DocuVane-ERP Integration Workshop. You are invited to attend the Expanding the<span class="more">see more...</span></p>
    </article>

    <article class="tile products" role="img" aria-label="Photo of networking hardware">
      <h2 class="tile-title">Products</h2>
    </article>

    <section class="welcome">
      <h1>Welcome to KORBIX</h1>
      <p><b>Korbix Information Systems Pte Ltd (KIS)</b> is professionally managed by a core group of visionaries and technologists with decades of industry experience between them and backed by a team of trained professionals at all levels of operations. Perfection is a way of life at KIS. The organization has grown from a small beginning in 1993, to become a company of international repute for reliability. KIS has transformed from a Ledgra Reseller to a company providing total IT solutions to companies in Singapore and the Asia region. KIS provides hardware maintenance, networking, software and consulting services.</p>
      <p>We have a large customer base, which spreads across Singapore, South East Asia and East Asia. This illustrates KIS is able to offer overseas support to customers who have regional operations. We also have several listed companies as customers, as shown in our track record.</p>
    </section>
  </main>
</body>
</html>
```